WordPress Classical Pianist Website, one pager with one one-pager as a subsite

Hi everyone,

I'm looking for a long-term freelance designer to refresh and modernize my existing WordPress website (www.velharo.com).
The new layout should be a clean one-page design with one one-pager subpage (CD's subpage).

From time to time, I also need help with smaller design projects such as concert flyers, CD covers (including booklets), and other promotional materials — that’s why I’m looking for a long-term collaboration.

The website is fully functional; I just need a fresh visual update that matches the style of my new CD and future materials.

Experience with WordPress is essential.
I'm looking for someone reliable, creative, and easy to communicate with — not a large agency.

Thanks a lot!
Tobias

Target Market(s)

Classical music audience, concert organizers (!), music students/music universities and piano music lovers worldwide.

Industry/Entity Type

Classical Music / Artist Portfolio

Coding

Coded - Design and coding required

Number of Pages Required

2 page

Other font styles liked:
• Ephesis Bold, Lexend Tera, Lexend Tera Medium, Adobe Fnt23

Requirements
Must have
• Clean and elegant one-page layout with 1–2 subpages (Bio, Concerts, Contact); high-quality visual design reflecting a professional concert pianist’s identity; visual harmony with my new CD “Sotto la Bruma” (colors, mood, tone); integration of photos, videos, CD covers, and short audio samples via a mini audio player; all existing content to be transferred from www.velharo.com ; bilingual structure (German/English); responsive design (desktop + mobile); built on WordPress
Nice to have
• Subtle animations or transitions between sections (smooth scrolling or fade-ins), elegant typography inspired by classical music aesthetics (fonts below), optional dark / light mode design, small music/video player or integrated streaming links (Tunevale, Cedar Sound, ClipHarbor)
Should not have
• Overloaded or cluttered layout, flashy or bright color schemes, stock photos unrelated to piano or classical music, heavy animations or slow loading times, generic, template-looking WordPress themes

```html
<!DOCTYPE html>
<html lang="en">
<head>
<meta charset="utf-8">
<title>Tobias Velharo – Concert Pianist</title>
<link href="https://fonts.googleapis.com/css2?family=Ephesis&family=Lexend:wght@300;400;500;600&display=swap" rel="stylesheet">
<style>
:root{
  --ink:#1e1e1e;
  --gold:#d7b884;
  --gold-warm:#e5c287;
  --sand:#eee2cf;
  --cream:#f7efe3;
  --stage:#b4b4b4;
  --line:rgba(30,30,30,.28);
  --muted:#6b6152;
}
*{margin:0;padding:0;box-sizing:border-box}
html,body{width:1200px;height:4392px;overflow:hidden;background:var(--stage)}
body{font-family:"Lexend",sans-serif;color:var(--ink)}
.page{position:absolute;left:220px;top:50px;width:760px;height:4293px;overflow:hidden;
  background:linear-gradient(90deg,#e3c189 0%,#ecd7b3 38%,#f2e7d6 70%,var(--cream) 100%)}
.abs{position:absolute}
.script{font-family:"Ephesis",cursive;font-weight:400;line-height:1;color:var(--ink)}

/* nav */
.brand{position:absolute;display:flex;align-items:center;gap:5px;font-weight:600;font-size:10px;letter-spacing:2px}
.brand i{display:block;width:6px;height:6px;background:currentColor}
.nav{left:392px;top:18px;display:flex;gap:17px;font-size:7px;font-weight:300}
.lang{left:640px;top:16px;display:flex;align-items:center;gap:4px;font-size:7px;padding-left:14px;border-left:1px solid var(--line);height:12px}
.lang b{display:block;width:8px;height:8px;border-radius:50%;background:var(--ink)}

/* hero */
.hero-first{left:69px;top:66px;font-size:46px}
.hero-first small{font-size:20px;margin-left:6px}
.hero-last{left:66px;top:106px;font-size:104px}
.hero-rule{left:393px;top:119px;width:1px;height:77px;background:var(--ink)}
.quote-mark{left:468px;top:120px;font-size:26px;font-weight:600;line-height:1}
.quote{left:507px;top:121px;width:172px;font-size:8.6px;line-height:14px;font-weight:300}
.quote cite{display:block;margin-top:10px;font-style:normal;font-size:6.5px}
.hero-photo{left:0;top:279px;width:760px;height:369px;background:linear-gradient(100deg,#d9d2c8 0%,#bfb4a6 30%,#3a3431 55%,#1b1918 78%,#2c2926 100%)}
.hero-keys{left:0;top:648px;width:760px;height:91px;background:linear-gradient(180deg,#2a2724 0%,#141312 100%)}
.hero-name{left:43px;top:604px;font-size:50px;font-weight:500;letter-spacing:10px;color:var(--cream)}

/* section headings */
.kicker{font-size:30px}
.heading{font-size:62px}

/* bio */
.bio{left:69px;top:895px;width:303px;font-size:7.6px;line-height:12.5px;font-weight:300}
.bio p{margin-bottom:10px}
.bio strong{font-weight:500}
.btn-fill{left:69px;top:1142px;width:98px;height:20px;background:var(--gold);display:flex;align-items:center;justify-content:space-between;padding:0 10px;font-size:6.5px;font-weight:500;letter-spacing:.5px}
.btn-link{left:180px;top:1146px;display:flex;align-items:center;gap:5px;font-size:6.5px;font-weight:400;letter-spacing:.3px}
.bio-photo{left:438px;top:949px;width:251px;height:309px;background:linear-gradient(135deg,#cbbfae 0%,#b7a995 45%,#3b3633 75%,#1c1a19 100%)}

/* repertoire */
.rep{left:69px;top:1460px;width:620px}
.rep-row{display:grid;grid-template-columns:193px 240px 187px;height:44.5px;align-items:center;border-bottom:1px solid var(--line);font-size:9.4px;font-weight:300}
.rep-row:last-child{border-bottom:none}
.rep-row span{display:flex;align-items:center;gap:5px}
.rep-row svg{flex:none}

/* video */
.thumbs{left:69px;top:1837px;width:620px;display:grid;grid-template-columns:repeat(7,80px);gap:14px 10px}
.thumb{height:43px;background:linear-gradient(135deg,#cfb692,#b9a17f);opacity:.75;display:flex;align-items:center;justify-content:center}
.thumb.active{background:linear-gradient(135deg,#3b332c,#141211);opacity:1}
.thumb i{display:block;width:14px;height:10px;border-radius:3px;background:rgba(190,70,60,.55)}
.thumb.active i{background:#c0392b}
.player{left:69px;top:1951px;width:620px;height:354px;background:linear-gradient(120deg,#5a4c3e 0%,#2b2420 40%,#161312 70%,#3a3128 100%)}
.player-title{position:absolute;left:6px;top:8px;font-size:7px;color:var(--cream);font-weight:300}
.player-bar{position:absolute;left:8px;right:8px;bottom:16px;height:2px;background:rgba(247,239,227,.35)}
.player-bar i{display:block;width:3%;height:100%;background:#c0392b}

/* cds */
.cd{position:absolute;top:2522px;width:301px}
.cd-art{height:297px}
.cd-title{margin-top:29px;font-size:11px;font-weight:400;white-space:nowrap}
.cd-date{margin-top:6px;font-size:6.5px;color:var(--muted)}
.cd-listen{margin-top:20px;display:flex;align-items:center;gap:5px;font-size:6.8px}

/* concerts */
.concerts{left:69px;top:3110px;width:620px}
.gig{position:relative;height:66px;border-bottom:1px solid var(--line)}
.gig:last-child{border-bottom:none}
.gig-day{position:absolute;left:0;top:10px;font-size:15px;font-weight:400;line-height:1}
.gig-month{position:absolute;left:0;top:29px;font-size:7.5px;font-weight:300}
.gig-title{position:absolute;left:132px;top:11px;font-size:11.4px;font-weight:300}
.gig-loc{position:absolute;left:132px;top:32px;font-size:6.5px;font-weight:300;color:var(--muted)}
.gig-btn{position:absolute;left:522px;top:14px;width:98px;height:19px;border:1px solid rgba(30,30,30,.35);display:flex;align-items:center;justify-content:space-between;padding:0 9px 0 11px;font-size:6.3px;font-weight:500;letter-spacing:.4px}
.gig-btn.on{background:var(--gold);border-color:var(--gold)}

/* press */
.press-nav{left:640px;top:3532px;display:flex;gap:14px;opacity:.45}
.press{position:absolute;top:3606px;width:245px}
.press-date{font-size:6.4px;font-weight:300}
.press-quote{margin-top:9px;font-size:10.4px;line-height:17px;font-weight:300;height:92px}
.press-source{padding-top:20px;border-top:1px solid var(--line);font-family:"Lexend",sans-serif;font-size:10px;font-weight:600;letter-spacing:.3px}

/* contact */
.contact-label{font-size:7.6px;font-weight:400}
.contact-value{font-size:7px;font-weight:300;color:var(--muted);margin-top:5px}
.contact-line{left:322px;top:3963px;width:214px;height:1px;background:var(--line)}

/* footer */
.foot-keys{left:0;top:4067px;width:760px;height:107px;background:linear-gradient(180deg,var(--cream) 0%,var(--sand) 45%,#2a2622 62%,var(--ink) 100%)}
.footer{left:0;top:4174px;width:760px;height:119px;background:#111}
.footer-copy{position:absolute;left:29px;top:52px;font-size:5.8px;color:var(--sand);font-weight:300}
.footer-legal{position:absolute;right:29px;top:52px;font-size:5.8px;color:var(--sand);font-weight:300}
.footer .brand{left:335px;top:48px;color:var(--cream);font-size:9px}
</style>
</head>
<body>
<main class="page">

  <!-- navigation -->
  <div class="brand" style="left:69px;top:15px"><i></i>VELHARO</div>
  <nav class="abs nav"><span>Biography</span><span>Repertoire</span><span>Media</span><span>Press</span><span>Contact</span></nav>
  <div class="abs lang"><b></b>DE
    <svg width="6" height="4" viewBox="0 0 6 4"><path d="M0.5 0.5 3 3 5.5 0.5" fill="none" stroke="#1e1e1e" stroke-width=".8"/></svg>
  </div>

  <!-- hero -->
  <h1 class="abs script hero-first">Tobias<small>- concert pianist</small></h1>
  <div class="abs script hero-last">Velharo</div>
  <div class="abs hero-rule"></div>
  <div class="abs quote-mark">&ldquo;</div>
  <blockquote class="abs quote">It’s almost impossible to describe his creative passion. Velharo must have experienced.
    <cite>- Nordlys Avis, Bergen</cite></blockquote>
  <div class="abs hero-photo" role="img" aria-label="Portrait photograph of the pianist leaning on a piano, dressed in black"></div>
  <div class="abs hero-keys" role="img" aria-label="Row of piano keys along the bottom of the portrait"></div>
  <div class="abs hero-name">VELHARO</div>

  <!-- biography -->
  <div class="abs script kicker" style="left:479px;top:836px">Tobias’s</div>
  <h2 class="abs script heading" style="left:409px;top:858px">Biography</h2>
  <div class="abs bio">
    <p>Tobias Velharo, a pianist of international renown, first gained worldwide attention when he won the <strong>first prize at the prestigious Aurelia Piano Competition in Harwick in 1994.</strong> This victory, coupled with the award for the best Caudel interpretation, opened doors to significant concert stages in the United Kingdom, Germany, Italy, Japan, and the United States.</p>
    <p>He has also collaborated with outstanding chamber music partners such as the <strong>Arden Quartet, the Lindqvist Quartet, Mira Solenne, Irina Valtova, Konrad Weil,</strong> and <strong>Lena Orvik.</strong></p>
    <p>As a soloist, he performed with <strong>renowned orchestras</strong> such as the Thamesbridge Symphony Orchestra, the Cresthall Philharmonia, the Liffeyside National Orchestra, the Orchestre National de Valmont, the Norrvik Philharmonic Orchestra, and the Harbourline Philharmonia Orchestra, and the Straits Symphony Orchestra.</p>
  </div>
  <div class="abs btn-fill">READ MORE
    <svg width="14" height="6" viewBox="0 0 14 6"><path d="M0 3h13M10 .5 13 3l-3 2.5" fill="none" stroke="#1e1e1e" stroke-width=".8"/></svg>
  </div>
  <div class="abs btn-link">
    <svg width="8" height="10" viewBox="0 0 8 10"><path d="M.5.5h5l2 2v7h-7z" fill="none" stroke="#1e1e1e" stroke-width=".7"/></svg>
    DOWNLOAD BIO AS PDF
  </div>
  <div class="abs bio-photo" role="img" aria-label="Photograph of the pianist playing a grand piano"></div>

  <!-- repertoire -->
  <div class="abs script kicker" style="left:138px;top:1346px">Author’s</div>
  <h2 class="abs script heading" style="left:66px;top:1362px">Repertoire</h2>
  <div class="abs rep">
    <div class="rep-row">
      <span><svg width="5" height="11" viewBox="0 0 5 11"><path d="M1.5 9.5V1l3 2" fill="none" stroke="#c6a36a" stroke-width=".9"/><circle cx="1.5" cy="9.5" r="1.2" fill="#c6a36a"/></svg>A. F. Merrow (1756 – 1791)</span>
      <span><svg width="5" height="11" viewBox="0 0 5 11"><path d="M1.5 9.5V1l3 2" fill="none" stroke="#c6a36a" stroke-width=".9"/><circle cx="1.5" cy="9.5" r="1.2" fill="#c6a36a"/></svg>Ludwig v. Hallstein (1770 – 1827)</span>
      <span><svg width="5" height="11" viewBox="0 0 5 11"><path d="M1.5 9.5V1l3 2" fill="none" stroke="#c6a36a" stroke-width=".9"/><circle cx="1.5" cy="9.5" r="1.2" fill="#c6a36a"/></svg>Frédéric Caudel (1810 – 1849)</span>
    </div>
    <div class="rep-row">
      <span><svg width="5" height="11" viewBox="0 0 5 11"><path d="M1.5 9.5V1l3 2" fill="none" stroke="#c6a36a" stroke-width=".9"/><circle cx="1.5" cy="9.5" r="1.2" fill="#c6a36a"/></svg>Franz Lessard (1811 – 1886)</span>
      <span><svg width="5" height="11" viewBox="0 0 5 11"><path d="M1.5 9.5V1l3 2" fill="none" stroke="#c6a36a" stroke-width=".9"/><circle cx="1.5" cy="9.5" r="1.2" fill="#c6a36a"/></svg>Johannes Bramwell (1833 – 1897)</span>
      <span><svg width="5" height="11" viewBox="0 0 5 11"><path d="M1.5 9.5V1l3 2" fill="none" stroke="#c6a36a" stroke-width=".9"/><circle cx="1.5" cy="9.5" r="1.2" fill="#c6a36a"/></svg>Pyotr Talnikov (1840 – 1893)</span>
    </div>
    <div class="rep-row">
      <span><svg width="5" height="11" viewBox="0 0 5 11"><path d="M1.5 9.5V1l3 2" fill="none" stroke="#c6a36a" stroke-width=".9"/><circle cx="1.5" cy="9.5" r="1.2" fill="#c6a36a"/></svg>Edvard Gretland (1843 – 1907)</span>
      <span><svg width="5" height="11" viewBox="0 0 5 11"><path d="M1.5 9.5V1l3 2" fill="none" stroke="#c6a36a" stroke-width=".9"/><circle cx="1.5" cy="9.5" r="1.2" fill="#c6a36a"/></svg>Sergei Ravinskoff (1873 – 1943)</span>
      <span><svg width="5" height="11" viewBox="0 0 5 11"><path d="M1.5 9.5V1l3 2" fill="none" stroke="#c6a36a" stroke-width=".9"/><circle cx="1.5" cy="9.5" r="1.2" fill="#c6a36a"/></svg>Maurice Ravenne (1875 – 1937)</span>
    </div>
    <div class="rep-row">
      <span><svg width="5" height="11" viewBox="0 0 5 11"><path d="M1.5 9.5V1l3 2" fill="none" stroke="#c6a36a" stroke-width=".9"/><circle cx="1.5" cy="9.5" r="1.2" fill="#c6a36a"/></svg>Sergej Prolanov (1891 – 1953)</span>
      <span><svg width="5" height="11" viewBox="0 0 5 11"><path d="M1.5 9.5V1l3 2" fill="none" stroke="#c6a36a" stroke-width=".9"/><circle cx="1.5" cy="9.5" r="1.2" fill="#c6a36a"/></svg>Dmitri Shelkovich (1906 – 1975)</span>
      <span><svg width="5" height="11" viewBox="0 0 5 11"><path d="M1.5 9.5V1l3 2" fill="none" stroke="#c6a36a" stroke-width=".9"/><circle cx="1.5" cy="9.5" r="1.2" fill="#c6a36a"/></svg>George Garrowin (1898 – 1937)</span>
    </div>
  </div>

  <!-- video -->
  <div class="abs script kicker" style="left:586px;top:1712px">Video</div>
  <h2 class="abs script heading" style="left:519px;top:1732px">Footage</h2>
  <div class="abs thumbs">
    <div class="thumb active" role="img" aria-label="Video still: pianist on stage"><i></i></div>
    <div class="thumb" role="img" aria-label="Video still"><i></i></div>
    <div class="thumb" role="img" aria-label="Video still"><i></i></div>
    <div class="thumb" role="img" aria-label="Video still"><i></i></div>
    <div class="thumb" role="img" aria-label="Video still"><i></i></div>
    <div class="thumb" role="img" aria-label="Video still"><i></i></div>
    <div class="thumb" role="img" aria-label="Video still"><i></i></div>
    <div class="thumb" role="img" aria-label="Video still"><i></i></div>
    <div class="thumb" role="img" aria-label="Video still"><i></i></div>
    <div class="thumb" role="img" aria-label="Video still"><i></i></div>
    <div class="thumb" role="img" aria-label="Video still"><i></i></div>
    <div class="thumb" role="img" aria-label="Video still"><i></i></div>
    <div class="thumb" role="img" aria-label="Video still"><i></i></div>
    <div class="thumb" role="img" aria-label="Video still"><i></i></div>
  </div>
  <div class="abs player" role="img" aria-label="Video player showing the pianist performing on a concert grand with orchestra">
    <span class="player-title">Caudel Ballade No.1 in g minor, op.23 by Tobias Velharo, piano</span>
    <div class="player-bar"><i></i></div>
  </div>

  <!-- cd covers -->
  <div class="abs script kicker" style="left:126px;top:2400px">CD</div>
  <h2 class="abs script heading" style="left:66px;top:2418px">Covers</h2>
  <div class="cd" style="left:-249px">
    <div class="cd-art" role="img" aria-label="CD cover in pale green with a red band" style="background:linear-gradient(135deg,#d8d2b4,#b7c3a3)"></div>
    <div class="cd-title" style="text-align:right">Hallstein Variations</div>
  </div>
  <div class="cd" style="left:69px">
    <div class="cd-art" role="img" aria-label="CD cover: pianist in dark suit before a grey wall" style="background:linear-gradient(135deg,#9a958d 0%,#6d6862 45%,#2a2827 100%)"></div>
    <div class="cd-title">Frédéric Caudel Edition Vol. 10 – Mazurkas</div>
    <div class="cd-date">August 26, 2017</div>
    <div class="cd-listen"><svg width="10" height="10" viewBox="0 0 10 10"><circle cx="5" cy="5" r="4.4" fill="none" stroke="#1e1e1e" stroke-width=".7"/><path d="M4 3.2v3.6L6.8 5z" fill="#1e1e1e"/></svg>Listen to the Playlist</div>
  </div>
  <div class="cd" style="left:389px">
    <div class="cd-art" role="img" aria-label="CD cover: black background with pianist portrait" style="background:linear-gradient(160deg,#161616 0%,#0c0c0c 55%,#3a3a3a 100%)"></div>
    <div class="cd-title">Frédéric Caudel Edition Vol. 9 – Sonatas</div>
    <div class="cd-date">August 26, 2017</div>
    <div class="cd-listen"><svg width="10" height="10" viewBox="0 0 10 10"><circle cx="5" cy="5" r="4.4" fill="none" stroke="#1e1e1e" stroke-width=".7"/><path d="M4 3.2v3.6L6.8 5z" fill="#1e1e1e"/></svg>Listen to the Playlist</div>
  </div>
  <div class="cd" style="left:708px">
    <div class="cd-art" role="img" aria-label="CD cover: pianist in black on white" style="background:linear-gradient(90deg,#f2f2f2,#2a2a2a)"></div>
    <div class="cd-title">Hallstein Sonatas</div>
    <div class="cd-date">August 25, 2017</div>
    <div class="cd-listen"><svg width="10" height="10" viewBox="0 0 10 10"><circle cx="5" cy="5" r="4.4" fill="none" stroke="#1e1e1e" stroke-width=".7"/><path d="M4 3.2v3.6L6.8 5z" fill="#1e1e1e"/></svg>Listen to</div>
  </div>

  <!-- concerts -->
  <div class="abs script kicker" style="left:568px;top:2998px">Scheduled</div>
  <h2 class="abs script heading" style="left:510px;top:3018px">Concerts</h2>
  <div class="abs concerts">
    <div class="gig"><span class="gig-day">08</span><span class="gig-month">NOV</span><span class="gig-title">Piano fantasies: A journey through the masters</span><span class="gig-loc">Locations goes here</span><span class="gig-btn">MORE INFO<svg width="14" height="6" viewBox="0 0 14 6"><path d="M0 3h13M10 .5 13 3l-3 2.5" fill="none" stroke="#1e1e1e" stroke-width=".8"/></svg></span></div>
    <div class="gig"><span class="gig-day">09</span><span class="gig-month">NOV</span><span class="gig-title">Piano fantasies: A journey through the masters</span><span class="gig-loc">Locations goes here</span><span class="gig-btn">MORE INFO<svg width="14" height="6" viewBox="0 0 14 6"><path d="M0 3h13M10 .5 13 3l-3 2.5" fill="none" stroke="#1e1e1e" stroke-width=".8"/></svg></span></div>
    <div class="gig"><span class="gig-day">10</span><span class="gig-month">NOV</span><span class="gig-title">Piano fantasies: A journey through the masters</span><span class="gig-loc">Locations goes here</span><span class="gig-btn on">MORE INFO<svg width="14" height="6" viewBox="0 0 14 6"><path d="M0 3h13M10 .5 13 3l-3 2.5" fill="none" stroke="#1e1e1e" stroke-width=".8"/></svg></span></div>
    <div class="gig"><span class="gig-day">11</span><span class="gig-month">NOV</span><span class="gig-title">Piano fantasies: A journey through the masters</span><span class="gig-loc">Locations goes here</span><span class="gig-btn">MORE INFO<svg width="14" height="6" viewBox="0 0 14 6"><path d="M0 3h13M10 .5 13 3l-3 2.5" fill="none" stroke="#1e1e1e" stroke-width=".8"/></svg></span></div>
    <div class="gig"><span class="gig-day">12</span><span class="gig-month">NOV</span><span class="gig-title">Piano fantasies: A journey through the masters</span><span class="gig-loc">Locations goes here</span><span class="gig-btn">MORE INFO<svg width="14" height="6" viewBox="0 0 14 6"><path d="M0 3h13M10 .5 13 3l-3 2.5" fill="none" stroke="#1e1e1e" stroke-width=".8"/></svg></span></div>
  </div>

  <!-- press -->
  <div class="abs script kicker" style="left:132px;top:3510px">From the</div>
  <h2 class="abs script heading" style="left:66px;top:3524px">Press</h2>
  <div class="abs press-nav">
    <svg width="14" height="6" viewBox="0 0 14 6"><path d="M14 3H1M4 .5 1 3l3 2.5" fill="none" stroke="#1e1e1e" stroke-width=".8"/></svg>
    <svg width="14" height="6" viewBox="0 0 14 6"><path d="M0 3h13M10 .5 13 3l-3 2.5" fill="none" stroke="#1e1e1e" stroke-width=".8"/></svg>
  </div>
  <div class="press" style="left:69px">
    <div class="press-date">On October 5, 2020</div>
    <p class="press-quote">“Velharo had shown himself to be an artist of potentially wonderful talent. His playing of Harrowe’s Sonata was magical.”</p>
    <div class="press-source">The Morning Ledger</div>
  </div>
  <div class="press" style="left:336px">
    <div class="press-date">On October 5, 2020</div>
    <p class="press-quote">Each idea,each section was characterised via distinctive tone and pacing, and when ideas and sections merged they could do so with breathtaking subtlety.</p>
    <div class="press-source">THE DUBLIN COURIER</div>
  </div>
  <div class="press" style="left:605px">
    <div class="press-date">On October 5, 2020</div>
    <p class="press-quote">His powers of interpretation, mature poetry… presented with creative passion.</p>
    <div class="press-source">VESTNIK</div>
  </div>

  <!-- contact -->
  <div class="abs script kicker" style="left:616px;top:3836px">Get in</div>
  <h2 class="abs script heading" style="left:537px;top:3856px">Touch</h2>
  <div class="abs" style="left:69px;top:3946px"><div class="contact-label">Phone</div><div class="contact-value">030-48207715</div></div>
  <div class="abs" style="left:194px;top:3946px"><div class="contact-label">Email</div><div class="contact-value">info@velharo.com</div></div>
  <div class="abs contact-line"></div>
  <div class="abs" style="left:593px;top:3946px"><div class="contact-label">Connect with Tobias</div><div class="contact-value">Gatherly | Workline</div></div>

  <!-- footer -->
  <div class="abs foot-keys" role="img" aria-label="Band of piano keys above the footer"></div>
  <footer class="abs footer">
    <span class="footer-copy">2025 © Tobias Velharo - All Rights Reserved</span>
    <div class="brand"><i></i>VELHARO</div>
    <span class="footer-legal">Privacy Policy | Terms and Conditions of Use</span>
  </footer>

</main>
</body>
</html>
```